New Flyer Design Project - for sale units at The Lodge phase 3

on attached the A2 is full kitchen 1 bedroom, the A3 is gally kitchen and the B2 is the the 2 bedroom, on attached pictures the room with 2 queen beds is only for the 2 bedroom

This is going to be used to sale the units (real estate sale) so the layout could possibly be text and then pictures maybe 1 bedroom on one side and 2 on the back?

Experience the Modern Luxury of the New Phase 3 Building of the
Lodge at Harwell Bend

* Opening Spring 2019

* America's #17 Family Resort; Tennessee's Only Ranked Resort

1 Bedroom Bunk Suite (Galley Kitchen) - $199,000; Sleeps 6

* Private King Master Bedroom

* Bunk Bed Galley

* Granite Counters Throughout

* Fully Furnished with Custom Furnishings

* Private Balcony

* Equipped Galley Kitchen

* In Unit Laundry

* Queen Sleeper Sofa

1 Bedroom Bunk Suite (Full Kitchen) - $209,000; Sleeps 6

* Bunk Bed Galley

* Granite Counters throughout

* Equipped Full Kitchen

* Completely Furnished with Custom Furnishings

* Private Balcony

* In Unit Laundry

* Queen Sleeper Sofa

2 Bedroom Bunk Suite (Full Kitchen) - $249,000; Sleeps 10

* Private King Master Bedroom with On-Suite Bathroom

* Two Queen Bedroom

* Bunk Bed Galley

* Full Kitchen

* Private Balcony

* In Unit Laundry

* Queen Sleeper Sofa

Target Market(s)

people wanting to buy units in phase 3 of The Lodge at Harwell Bend

Industry/Entity Type

Real Estate Development

Requirements
Must have
• attached text to describe units and price
• pictures and layouts
• Contact Dale Corwin
• 865-731-9052 Dale@briarwoodvacationhomes.com
Nice to have
• brand and logo
Should not have
• it should not be plain this is m ore of a luxury project

```html
<!DOCTYPE html>
<html lang="en">
<head>
<meta charset="utf-8">
<title>The Lodge at Harwell Bend – Phase 3 Flyer</title>
<link rel="stylesheet" href="https://fonts.googleapis.com/css2?family=Merriweather:wght@700;900&family=Source+Sans+3:wght@400;600&display=swap">
<style>
  :root {
    --teal: #5e8491;
    --teal-text: #4a7482;
    --orange: #c98d4e;
    --orange-bright: #e58a2c;
    --ink: #222;
    --grey-dark: #4f4f4f;
    --brown: #6e4a2c;
    --footer-dark: #3d3d40;
    --stage: #b7b7b7;
    --paper: #ffffff;
  }
  * { margin: 0; padding: 0; box-sizing: border-box; }
  html, body { width: 960px; height: 1200px; overflow: hidden; }
  body {
    background: var(--stage);
    font-family: "Source Sans 3", Arial, sans-serif;
    color: var(--ink);
    position: relative;
  }
  .page {
    position: absolute;
    top: 282px;
    width: 450px;
    height: 636px;
    background: var(--paper);
    overflow: hidden;
    box-shadow: 0 8px 24px rgba(0,0,0,.35);
  }
  .page--front { left: 20px; }
  .page--back { left: 490px; }
  .page > svg.backdrop { position: absolute; inset: 0; }
  .abs { position: absolute; }

  /* Front */
  .headline { left: 24px; font-family: "Merriweather", Georgia, serif; font-weight: 900; font-size: 28px; line-height: 1; letter-spacing: .5px; }
  .headline--opening { top: 22px; color: var(--orange); }
  .headline--season { top: 52px; color: var(--grey-dark); }
  .rank { left: 24px; top: 90px; font-size: 18px; color: var(--teal-text); }
  .rank-sub { left: 24px; top: 111px; font-size: 14.5px; color: var(--ink); }
  .brand-name {
    left: 264px; width: 186px; top: 50px; text-align: center;
    font-family: "Merriweather", Georgia, serif; font-weight: 900; font-size: 26px; color: var(--brown);
  }
  .tagline { left: 24px; top: 556px; font-size: 13.5px; line-height: 16px; color: var(--teal-text); }
  .front-contact { left: 24px; top: 605px; font-size: 10px; color: #fff; }
  .front-contact .label { text-decoration: underline; display: block; margin-bottom: 3px; }
  .front-contact .row { color: var(--orange); display: flex; gap: 22px; align-items: center; }
  .front-contact .item { display: flex; align-items: center; gap: 4px; }

  .social { display: flex; gap: 8px; }
  .social span { width: 16px; height: 16px; border: 1.5px solid #333; border-radius: 50%; display: block; }
  .front-social { left: 388px; top: 614px; }

  /* Back */
  .suite-bar { left: 0; height: 20px; display: flex; font-size: 11px; font-weight: 600; }
  .suite-bar .title { width: 225px; background: var(--orange); padding-left: 20px; display: flex; align-items: center; gap: 9px; color: #3a2a1c; }
  .suite-bar .title em { font-style: normal; color: #fff; }
  .suite-bar .price { width: 132px; background: var(--teal); color: #fff; display: flex; align-items: center; justify-content: space-between; padding: 0 8px; }
  .suite-bar .price b { font-size: 14px; font-weight: 600; }
  .features { left: 20px; list-style: none; font-size: 9.6px; line-height: 13.6px; color: var(--teal-text); }
  .features li { display: flex; align-items: center; gap: 5px; }
  .features li::before { content: ""; width: 6px; height: 3px; border-left: 1.5px solid var(--orange); border-bottom: 1.5px solid var(--orange); transform: rotate(-45deg) translateY(-1px); }
  .floorplan { position: absolute; background: linear-gradient(135deg, #e6dccb, #cfc4b2); border: 2px solid #6b5a48; }
  .back-brand { left: 26px; top: 576px; font-family: "Merriweather", Georgia, serif; font-weight: 900; font-size: 24px; color: var(--brown); }
  .back-contact { left: 164px; top: 562px; font-size: 10px; color: #222; line-height: 15.5px; }
  .back-contact .label { text-decoration: underline; font-weight: 600; }
  .back-contact .indent { padding-left: 12px; display: flex; align-items: center; gap: 5px; }
  .follow { left: 362px; top: 562px; font-size: 10px; font-weight: 600; text-decoration: underline; }
  .back-social { left: 362px; top: 582px; }
  .back-social span { width: 19px; height: 19px; }
</style>
</head>
<body>

<!-- Front side -->
<section class="page page--front">
  <svg class="backdrop" width="450" height="636" viewBox="0 0 450 636">
    <defs>
      <linearGradient id="sheen" x1="0" y1="0" x2="1" y2="1">
        <stop offset="0" stop-color="#ffffff"/><stop offset="1" stop-color="#e6e8ea"/>
      </linearGradient>
      <linearGradient id="interior" x1="0" y1="0" x2="1" y2="1">
        <stop offset="0" stop-color="#9aa46c"/><stop offset=".5" stop-color="#c9c2a8"/><stop offset="1" stop-color="#4a4440"/>
      </linearGradient>
      <radialGradient id="room" cx=".5" cy=".5" r=".6">
        <stop offset="0" stop-color="#d9d3c1"/><stop offset="1" stop-color="#8f9468"/>
      </radialGradient>
    </defs>
    <rect width="450" height="636" fill="url(#sheen)"/>
    <!-- logo pennant -->
    <polygon points="264,0 450,0 450,122 357,146 264,122" fill="#dadcde"/>
    <!-- teal wave bands -->
    <path d="M0,170 C140,140 300,150 450,160 L450,425 C300,400 150,405 0,420 Z" fill="var(--teal)"/>
    <path d="M0,170 C140,140 300,150 450,160" fill="none" stroke="var(--orange)" stroke-width="2"/>
    <!-- main photo -->
    <path role="img" aria-label="Photo of the suite's dining area and granite kitchen island" d="M0,190 C150,165 300,172 450,178 L450,382 C300,392 150,378 0,398 Z" fill="url(#interior)"/>
    <!-- lower white swoosh -->
    <path d="M0,432 C150,405 300,400 450,405 L450,636 L0,636 Z" fill="url(#sheen)"/>
    <!-- room circles -->
    <circle role="img" aria-label="Photo of the dining table and kitchen" cx="92" cy="446" r="62" fill="url(#room)" stroke="var(--brown)" stroke-width="4"/>
    <circle role="img" aria-label="Photo of a queen bedroom" cx="232" cy="446" r="62" fill="url(#room)" stroke="var(--brown)" stroke-width="4"/>
    <circle role="img" aria-label="Photo of the bathroom vanity" cx="370" cy="446" r="62" fill="url(#room)" stroke="var(--brown)" stroke-width="4"/>
    <!-- footer -->
    <rect x="340" y="594" width="110" height="42" fill="var(--orange)"/>
    <path d="M0,594 L358,594 A21,21 0 0 1 358,636 L0,636 Z" fill="var(--footer-dark)"/>
  </svg>

  <div class="abs headline headline--opening">OPENING</div>
  <div class="abs headline headline--season">SPRING 2019</div>
  <div class="abs rank">America's #17 Family Resort</div>
  <div class="abs rank-sub">Tennessee's Only Ranked Resort</div>
  <div class="abs brand-name">The Lodge</div>

  <p class="abs tagline">Experience the Modern Luxury of the New Phase 3 Building<br>of the Lodge at Harwell Bend</p>

  <div class="abs front-contact">
    <span class="label">Contact</span>
    <div class="row">
      <span>Dale Corwin</span>
      <span class="item">
        <svg width="9" height="9" viewBox="0 0 10 10"><path d="M2,1 L4,1 L5,3 L4,4 C4.5,5.5 5,6 6,6 L7,5 L9,6 L9,8 C9,9 8,9 7,9 C4,9 1,6 1,3 C1,2 1,1 2,1 Z" fill="var(--orange)"/></svg>
        865-731-9052
      </span>
      <span class="item">
        <svg width="9" height="9" viewBox="0 0 10 10"><circle cx="5" cy="5" r="4.5" fill="var(--orange)"/></svg>
        Dale@briarwoodvacationhomes.com
      </span>
    </div>
  </div>
  <div class="abs social front-social"><span></span><span></span></div>
</section>

<!-- Back side -->
<section class="page page--back">
  <svg class="backdrop" width="450" height="636" viewBox="0 0 450 636">
    <defs>
      <linearGradient id="foot" x1="0" y1="0" x2="1" y2="0">
        <stop offset="0" stop-color="#cfd1d3"/><stop offset=".6" stop-color="#eceded"/><stop offset="1" stop-color="#d6d8da"/>
      </linearGradient>
    </defs>
    <path d="M0,0 L450,0 L450,24 C300,40 150,30 0,38 Z" fill="var(--teal)"/>
    <path d="M0,38 C150,30 300,40 450,24 L450,60 C300,44 150,52 0,58 Z" fill="#f1f2f3"/>
    <path d="M0,548 C150,538 300,536 450,540 L450,636 L0,636 Z" fill="url(#foot)"/>
    <rect y="632" width="450" height="4" fill="var(--orange-bright)"/>
  </svg>

  <!-- Suite A3 -->
  <div class="abs suite-bar" style="top:58px">
    <div class="title">1 Bedroom Bunk Suite <em>(Galley Kitchen) -</em></div>
    <div class="price"><b>$199,000</b><span>Sleeps 6</span></div>
  </div>
  <ul class="abs features" style="top:87px">
    <li>Private King Master Bedroom</li>
    <li>Bunk Bed Galley</li>
    <li>Granite Counters Throughout</li>
    <li>Fully Furnished with Custom Furnishings</li>
    <li>Private Balcony</li>
    <li>Equipped Galley Kitchen</li>
    <li>In Unit Laundry</li>
    <li>Queen Sleeper Sofa</li>
  </ul>
  <div class="floorplan" role="img" aria-label="Floor plan of the 1 bedroom galley kitchen suite" style="left:313px;top:82px;width:120px;height:120px"></div>

  <!-- Suite A2 -->
  <div class="abs suite-bar" style="top:215px">
    <div class="title">1 Bedroom Bunk Suite <em>(Full Kitchen) -</em></div>
    <div class="price"><b>$209,000</b><span>Sleeps 6</span></div>
  </div>
  <ul class="abs features" style="top:243px">
    <li>Private King Master Bedroom</li>
    <li>Bunk Bed Galley</li>
    <li>Granite Counters throughout</li>
    <li>Equipped Full Kitchen</li>
    <li>Completely Furnished with Custom Furnishings</li>
    <li>Private Balcony</li>
    <li>In Unit Laundry</li>
    <li>Queen Sleeper Sofa</li>
  </ul>
  <div class="floorplan" role="img" aria-label="Floor plan of the 1 bedroom full kitchen suite" style="left:299px;top:244px;width:133px;height:107px"></div>

  <!-- Suite B2 -->
  <div class="abs suite-bar" style="top:370px">
    <div class="title">2 Bedroom Bunk Suite <em>(Full Kitchen) -</em></div>
    <div class="price"><b>$249,000</b><span>Sleeps 10</span></div>
  </div>
  <ul class="abs features" style="top:397px">
    <li>Private King Master Bedroom with On-Suite Bathroom</li>
    <li>Two Queen Bedroom</li>
    <li>Bunk Bed Galley</li>
    <li>Granite Counters Throughout</li>
    <li>Full Kitchen</li>
    <li>Completely Furnished with Custom Furnishings</li>
    <li>Private Balcony</li>
    <li>In Unit Laundry</li>
    <li>Queen Sleeper Sofa</li>
  </ul>
  <div class="floorplan" role="img" aria-label="Floor plan of the 2 bedroom suite" style="left:310px;top:395px;width:113px;height:132px"></div>

  <!-- Footer -->
  <div class="abs back-brand">The Lodge</div>
  <div class="abs back-contact">
    <div class="label">Contact</div>
    <div class="indent">Dale Corwin</div>
    <div class="indent">
      <svg width="9" height="9" viewBox="0 0 10 10"><path d="M2,1 L4,1 L5,3 L4,4 C4.5,5.5 5,6 6,6 L7,5 L9,6 L9,8 C9,9 8,9 7,9 C4,9 1,6 1,3 C1,2 1,1 2,1 Z" fill="var(--orange-bright)"/></svg>
      865-731-9052
    </div>
    <div class="indent">
      <svg width="9" height="9" viewBox="0 0 10 10"><circle cx="5" cy="5" r="4.5" fill="var(--orange-bright)"/></svg>
      Dale@briarwoodvacationhomes.com
    </div>
  </div>
  <div class="abs follow">Follow Us</div>
  <div class="abs social back-social"><span></span><span></span></div>
</section>

</body>
</html>
```